Bref créative
Brochure project
The home with two doors
Start believing in your future
Content within Brochure:
Programs for agents, brokers and Independently Owned and Operated Brokerages (Brisvale Mortgage Partners)
Brisvale Branded Mortgages & Alternative Mortgage Products
Leading edge tools – CRM, Marketing Campaign Software, Doc Management Software, Learning Resource Center, and more!
FREE Websites – add/create/delete pages at any time and is fully integrated with the CRM software
Leading Payroll Management Process – paying 2 times per week, 8 times per month, 96 times per year.
Revenue Diversity Strategy – GIC, Leasing, Dedicated Commercial Mortgage department and more.
Strong commitment to ongoing training and support
-> Weekly, monthly, quarterly training events
Access to Brisvale’s Central Underwriting Unit to grant you access to lenders, products, and competitive pricing
As one of the fastest growing organization’s in our industry Brisvale is now represented by 600 mortgage professionals across Canada
Consulting
Corporate (B2B), Mortgage Agents and Brokers. This is strictly targeting a business audience in the mortgage and banking industry.
The purpose of this brochure is to recruit more agents and brokers to our organization. I want the ad to be unique, creative and highly professional. Detail is key here, we want the audience to see an ad that surpasses our competitors. This would be placed in the http://www.lendingdeskweekly.ca mortgage magazine called the "HLQ". This ad will be for Brisvale Mortgage Corporation and Finance, www.brisvalemortgages.ca. I can provide EPS logo upon request.

```html
<!DOCTYPE html>
<html lang="en">
<head>
<meta charset="utf-8">
<title>Brisvale Mortgages – Start Believing in Your Future</title>
<link href="https://fonts.googleapis.com/css2?family=Libre+Baskerville:ital,wght@0,400;0,700;1,400;1,700&family=Open+Sans:ital,wght@0,400;0,600;0,700;1,600;1,700&display=swap" rel="stylesheet">
<style>
  :root {
    --navy: #1d3a72;
    --blue: #2b5fae;
    --sky: #6f9bd6;
    --ink: #2a2f38;
    --paper: #ffffff;
    --stage: #e6e8ec;
    --photo-light: #eef1f5;
    --photo-mid: #c9d3e0;
    --photo-dark: #5c6f8c;
  }
  * { box-sizing: border-box; margin: 0; padding: 0; }
  html, body { width: 1200px; height: 794px; overflow: hidden; }
  body {
    background: var(--stage);
    font-family: "Open Sans", Arial, sans-serif;
    color: var(--ink);
    position: relative;
  }
  .flyer {
    position: absolute;
    left: 347px; top: 12px;
    width: 506px; height: 770px;
    background: var(--paper);
    box-shadow: 0 4px 18px rgba(0,0,0,.18);
    overflow: hidden;
  }
  .hero {
    position: absolute; left: 0; top: 0;
    width: 100%; height: 372px;
  }
  .hero-photo {
    position: absolute; inset: 0;
    background:
      radial-gradient(ellipse at 68% 60%, #f4f1ee 0 18%, transparent 40%),
      linear-gradient(110deg, var(--photo-light) 0%, var(--photo-mid) 45%, var(--photo-light) 62%, var(--photo-dark) 100%);
  }
  .tagline {
    position: absolute; left: 0; top: 238px;
    width: 196px; height: 134px;
    background: rgba(255,255,255,.93);
    padding: 12px 0 0 18px;
    font-family: "Libre Baskerville", Georgia, serif;
    line-height: 1.05;
  }
  .tagline span { display: block; }
  .tagline .caps { font-size: 25px; color: var(--navy); letter-spacing: .5px; }
  .tagline .word { font-size: 25px; color: var(--blue); }
  .tagline .small { font-size: 21px; color: var(--navy); }
  .tagline .rule {
    height: 2px; background: var(--sky); width: 160px; margin: 3px 0;
  }
  .hero-band {
    position: absolute; left: 0; top: 372px;
    width: 100%; height: 10px;
    background: var(--navy);
    border-bottom: 3px solid var(--sky);
  }
  .content {
    position: absolute; left: 22px; right: 22px; top: 396px;
    font-size: 8.3px; line-height: 1.38;
  }
  .intro {
    font-family: "Libre Baskerville", Georgia, serif;
    font-style: italic; font-weight: 700;
    font-size: 13.6px; line-height: 1.28;
    color: var(--blue);
    margin-bottom: 9px;
  }
  .section-title {
    font-weight: 700; font-size: 9px; color: var(--navy);
    text-transform: uppercase; letter-spacing: .2px;
    margin-bottom: 3px;
  }
  .benefits { list-style: none; margin-bottom: 9px; }
  .benefits li { margin-bottom: 1px; }
  .benefits strong, .training strong { color: var(--blue); font-weight: 700; }
  .training { margin-bottom: 9px; }
  .growth {
    font-style: italic; font-weight: 700;
    font-size: 12.3px; line-height: 1.3; color: var(--navy);
  }
  .growth .count { font-size: 16px; color: var(--blue); }
  .footer {
    position: absolute; left: 0; top: 668px;
    width: 100%; height: 68px;
    display: flex; align-items: center;
    padding: 0 18px;
  }
  .brand {
    display: flex; align-items: center; gap: 8px;
    width: 172px;
  }
  .brand-dot {
    width: 20px; height: 20px; border-radius: 50%;
    background: var(--navy);
  }
  .brand-name {
    font-family: "Open Sans", Arial, sans-serif;
    font-weight: 700; font-size: 28px; color: var(--navy);
  }
  .slogan {
    font-family: "Libre Baskerville", Georgia, serif;
    font-style: italic; color: var(--navy);
    font-size: 17px; line-height: 1.05;
    width: 160px;
  }
  .slogan b { color: var(--blue); font-weight: 700; }
  .contact {
    font-size: 7px; line-height: 1.45; color: var(--ink);
  }
  .url-bar {
    position: absolute; left: 0; bottom: 0;
    width: 100%; height: 34px;
    background: var(--navy);
    color: var(--paper);
    display: flex; align-items: center; justify-content: center;
    font-weight: 700; font-size: 17px; letter-spacing: .6px;
  }
</style>
</head>
<body>
  <article class="flyer">
    <header class="hero">
      <div class="hero-photo" role="img" aria-label="Office photo of a smiling businesswoman at a desk with colleagues meeting in the background"></div>
      <h1 class="tagline">
        <span class="caps">START</span>
        <span class="word">believing</span>
        <span class="rule"></span>
        <span class="small">in Your</span>
        <span class="caps">FUTURE</span>
      </h1>
    </header>
    <div class="hero-band"></div>

    <section class="content">
      <h2 class="intro">Programs for agents, brokers &amp; Independently Owned and Operated Brokerages (Brisvale Mortgage Partners)</h2>

      <h3 class="section-title">Brisvale Branded Mortgages &amp; Alternative Mortgage Products</h3>
      <ul class="benefits">
        <li><strong>Leading Edge Tools</strong> – CRM, Marketing Campaign Software, Doc Management Software, Learning Resource Center, and more!</li>
        <li><strong>Free Websites</strong> – add/create/delete pages at any time and is fully integrated with the CRM software</li>
        <li><strong>Leading Payroll Management Process</strong> – paying 2 times per week, 8 times per month, 96 times per year</li>
        <li><strong>Revenue Diversity Strategy</strong> – GIC, Leasing, Dedicated Commercial Mortgage department and more</li>
      </ul>

      <h3 class="section-title">Strong Commitment to Ongoing Training and Support</h3>
      <p class="training"><strong>Weekly, monthly, quarterly training events</strong><br>
        Access to Brisvale’s Central Underwriting Unit to grant you access to lenders, products, and competitive pricing</p>

      <p class="growth">As one of the fastest growing organization’s in our industry Brisvale is now represented by <span class="count">600</span> mortgage professionals across Canada.</p>
    </section>

    <footer class="footer">
      <div class="brand">
        <span class="brand-dot"></span>
        <span class="brand-name">Brisvale</span>
      </div>
      <p class="slogan">The Home with <b>two DOOR</b></p>
      <address class="contact" style="font-style:normal">
        4150 Harbour Road, Suite 210<br>
        Milton Ontario L9T 0A1, Canada<br>
        Phone: (905) 555-0142<br>
        Fax: (905) 555-0178<br>
        Email: info@brisvalemortgages.ca
      </address>
    </footer>
    <div class="url-bar">www.brisvalemortgages.ca</div>
  </article>
</body>
</html>
```